Testosterone clinic billboard

Design billboard for Male Testosterone therapy simple to the point but eye catching.
Contact info for the billboard - Vantoraclinic.com
Phone - 555-274-6180

Target Market(s)

Males with disposable income

Industry/Entity Type

medical

Requirements
Must have
• Testosterone Therapy, Erectile Dysfunction, Male Enhancement
Nice to have
• Simple, easy to read

```html
<!DOCTYPE html>
<html lang="en">
<head>
<meta charset="utf-8">
<title>Vantoraclinic Billboard</title>
<link href="https://fonts.googleapis.com/css2?family=Barlow+Condensed:wght@600&display=swap" rel="stylesheet">
<style>
  :root {
    --purple: #6a1b78;
    --teal: #006b66;
    --teal-light: #14a7a0;
    --white: #ffffff;
    --ink: #111111;
    --backdrop: #ececec;
  }
  html, body {
    margin: 0;
    padding: 0;
    width: 1200px;
    height: 1200px;
    overflow: hidden;
    background: var(--backdrop);
  }
  .canvas {
    position: relative;
    width: 1200px;
    height: 1200px;
    display: flex;
    align-items: center;
    justify-content: center;
  }
  .billboard {
    display: block;
    width: 1110px;
    height: 323px;
  }
  .service-label,
  .brand-name,
  .contact-text {
    font-family: "Barlow Condensed", "Arial Narrow", sans-serif;
    font-weight: 600;
  }
  .service-label { fill: var(--white); font-size: 42px; }
  .brand-name { fill: var(--purple); font-size: 72px; }
  .contact-text { fill: var(--white); font-size: 48px; }
  .icon-line { fill: none; stroke: var(--ink); stroke-width: 5; stroke-linecap: round; stroke-linejoin: round; }
</style>
</head>
<body>
<main class="canvas">
  <svg class="billboard" viewBox="0 0 1785 520" xmlns="http://www.w3.org/2000/svg">
    <defs>
      <linearGradient id="photo-tone" x1="0" y1="0" x2="1" y2="1">
        <stop offset="0" stop-color="#8f9a3c"/>
        <stop offset="0.45" stop-color="#b9b46a"/>
        <stop offset="1" stop-color="#d6c48a"/>
      </linearGradient>
    </defs>

    <rect class="photo-area" role="img" aria-label="Photo of a smiling man hugging his dog outdoors in a sunny park" x="0" y="0" width="780" height="520" fill="url(#photo-tone)"/>

    <path class="corner-teal" d="M0,372 C120,455 250,505 420,520 H0 Z" fill="var(--teal)"/>
    <path class="corner-purple" d="M0,410 C110,470 220,505 350,520 H0 Z" fill="var(--purple)"/>

    <path class="sweep-teal" d="M700,0 H780 C755,200 710,330 640,395 L520,520 H410 C570,470 675,320 700,0 Z" fill="var(--teal)"/>

    <path class="service-panel" d="M770,0 H1785 V395 H640 C705,330 745,200 770,0 Z" fill="var(--purple)"/>

    <path class="brand-strip" d="M640,395 H1080 C1070,450 1050,490 1015,520 H455 C540,490 600,445 640,395 Z" fill="var(--white)"/>

    <path class="contact-accent" d="M1062,395 H1085 C1080,450 1060,490 1030,520 H1010 C1045,490 1060,450 1062,395 Z" fill="var(--teal-light)"/>
    <path class="contact-band" d="M1080,395 H1785 V520 H1022 C1055,490 1075,450 1080,395 Z" fill="var(--teal)"/>

    <line x1="1110" y1="75" x2="1110" y2="322" stroke="var(--white)" stroke-width="3"/>
    <line x1="1435" y1="75" x2="1435" y2="322" stroke="var(--white)" stroke-width="3"/>

    <!-- Service: Testosterone Therapy (plus) -->
    <g class="service">
      <circle cx="928" cy="138" r="70" fill="var(--white)"/>
      <path class="icon-line" d="M928,112 v52 M902,138 h52"/>
      <text class="service-label" x="928" y="252" text-anchor="middle">Testosterone</text>
      <text class="service-label" x="928" y="305" text-anchor="middle">Therapy</text>
    </g>

    <!-- Service: Erectile Dysfunction (tick) -->
    <g class="service">
      <circle cx="1270" cy="138" r="70" fill="var(--white)"/>
      <path class="icon-line" d="M1244,140 l17,17 l33,-36"/>
      <text class="service-label" x="1270" y="252" text-anchor="middle">Erectile</text>
      <text class="service-label" x="1270" y="305" text-anchor="middle">Dysfunction</text>
    </g>

    <!-- Service: Male Enhancement (up arrow) -->
    <g class="service">
      <circle cx="1586" cy="138" r="70" fill="var(--white)"/>
      <path class="icon-line" d="M1586,166 v-54 M1564,134 l22,-22 l22,22"/>
      <text class="service-label" x="1586" y="252" text-anchor="middle">Male</text>
      <text class="service-label" x="1586" y="305" text-anchor="middle">Enhancement</text>
    </g>

    <text class="brand-name" x="835" y="482" text-anchor="middle">Vantoraclinic</text>

    <g class="contact-phone">
      <path d="M1097,450 c-3,3 -2,10 6,18 s15,9 18,6 l3,-3 -6,-6 -4,3 c-3,-1 -7,-5 -8,-8 l3,-4 -6,-6 Z" fill="var(--white)"/>
      <text class="contact-text" x="1133" y="474">555-274-6180</text>
    </g>

    <g class="contact-web">
      <circle cx="1403" cy="460" r="11" fill="none" stroke="var(--white)" stroke-width="3"/>
      <path d="M1392,460 h22 M1403,449 c-6,6 -6,16 0,22 c6,-6 6,-16 0,-22" fill="none" stroke="var(--white)" stroke-width="2.5"/>
      <text class="contact-text" x="1425" y="474">Vantoraclinic.com</text>
    </g>
  </svg>
</main>
</body>
</html>
```